Business Card Design for a Lending Business (Hard Money loans)

We need a business card for our Real Estate Lending business. We do hard Money loans for real estate investors. We have an existing logo we like, see attached. I'd like the business card to mostly include the logo colors, but a bright color pop of some sort would be nice to see also. Card should include Logo, Company Name, Company Address, Employee Name, Cell Phone, Main Phone, Email, Website

Industry/Entity Type

Finance / Lending

Contact Information for Business Card

Logo, Company Name, Company Address, Employee Name, Cell Phone, Main Phone, Email, Website

Requirements
Nice to have
• I'd like the business card to mostly include the logo colors, but a bright color pop of some sort would be nice to see also.

```html
<!DOCTYPE html>
<html lang="en">
<head>
<meta charset="utf-8">
<title>Ridgeline Lending – Business Card</title>
<link href="https://fonts.googleapis.com/css2?family=Montserrat:wght@400;500;700&display=swap" rel="stylesheet">
<style>
  :root {
    --backdrop: #1c1c1e;
    --navy: #0b2a8f;
    --royal: #0d3fb8;
    --sky: #13a8e0;
    --ink: #1e1e24;
    --paper: #ffffff;
  }
  * { box-sizing: border-box; margin: 0; padding: 0; }
  html, body { width: 1200px; height: 800px; overflow: hidden; }
  body {
    background: var(--backdrop);
    font-family: "Montserrat", sans-serif;
    display: flex;
    align-items: center;
    justify-content: center;
    gap: 60px;
  }
  .card {
    width: 510px;
    height: 292px;
    border-radius: 26px;
    position: relative;
    overflow: hidden;
  }
  .card-front {
    background: var(--paper);
    border: 2px solid var(--royal);
    display: flex;
  }
  .front-brand {
    width: 46%;
    display: flex;
    align-items: center;
    justify-content: center;
  }
  .divider {
    width: 2px;
    margin: 40px 0;
    background: linear-gradient(to bottom, transparent, var(--navy) 20%, var(--navy) 80%, transparent);
  }
  .front-details {
    flex: 1;
    padding: 44px 0 0 22px;
  }
  .brand-name {
    display: flex;
    align-items: center;
    gap: 10px;
    font-weight: 700;
    font-size: 22px;
    letter-spacing: 2px;
    line-height: 1.15;
    color: var(--navy);
  }
  .brand-dot {
    width: 22px;
    height: 22px;
    border-radius: 50%;
    background: var(--sky);
    flex: none;
  }
  .person-name {
    font-weight: 700;
    font-size: 21px;
    color: var(--navy);
    letter-spacing: 0.5px;
  }
  .person-title {
    font-size: 11.5px;
    font-weight: 500;
    color: var(--ink);
    letter-spacing: 0.6px;
    margin-top: 3px;
  }
  .contact-list {
    list-style: none;
    margin-top: 14px;
  }
  .contact-list li {
    display: flex;
    align-items: center;
    gap: 8px;
    font-size: 12px;
    color: var(--ink);
    line-height: 1.55;
  }
  .contact-list svg { width: 12px; height: 12px; flex: none; }
  .address {
    font-size: 12px;
    color: var(--ink);
    line-height: 1.45;
    margin-top: 2px;
  }
  .card-back {
    background: radial-gradient(circle at 52% 42%, #16b4ec 0%, #0b6fd0 30%, #0b3fb0 62%, #0a2a8a 100%);
    display: flex;
    align-items: center;
    justify-content: center;
  }
  .card-back .brand-name {
    color: var(--paper);
    font-size: 30px;
    letter-spacing: 3px;
    gap: 14px;
  }
  .card-back .brand-dot { width: 30px; height: 30px; background: var(--paper); }
</style>
</head>
<body>

<section class="card card-front" aria-label="Business card front">
  <div class="front-brand">
    <div class="brand-name"><span class="brand-dot"></span><span>RIDGELINE<br>LENDING</span></div>
  </div>
  <div class="divider"></div>
  <div class="front-details">
    <h1 class="person-name">DANIEL HART</h1>
    <p class="person-title">MANAGING DIRECTOR</p>
    <ul class="contact-list">
      <li>
        <svg viewBox="0 0 12 12"><rect x="3" y="0.8" width="6" height="10.4" rx="1.2" fill="none" stroke="#13a8e0" stroke-width="1.2"/><circle cx="6" cy="9.4" r="0.6" fill="#13a8e0"/></svg>
        044-555 210 347
      </li>
      <li>
        <svg viewBox="0 0 12 12"><path d="M2.5 1.5l2 .3.7 2.2-1.2 1a6 6 0 0 0 3 3l1-1.2 2.2.7.3 2a1 1 0 0 1-1 1A9 9 0 0 1 1.5 2.5a1 1 0 0 1 1-1z" fill="#13a8e0"/></svg>
        044-555 210 348
      </li>
      <li>
        <svg viewBox="0 0 12 12"><rect x="0.8" y="2.2" width="10.4" height="7.6" rx="0.8" fill="#13a8e0"/><path d="M1 2.6l5 4 5-4" fill="none" stroke="#fff" stroke-width="1"/></svg>
        info@ridgelinelend.com
      </li>
      <li>
        <svg viewBox="0 0 12 12"><circle cx="6" cy="6" r="5" fill="#13a8e0"/><path d="M1 6h10M6 1c-2.2 2.8-2.2 7.2 0 10M6 1c2.2 2.8 2.2 7.2 0 10" fill="none" stroke="#fff" stroke-width="0.8"/></svg>
        www.ridgelinelend.com
      </li>
    </ul>
    <p class="address">421, Address line goes here<br>45452, Country name</p>
  </div>
</section>

<section class="card card-back" aria-label="Business card back">
  <div class="brand-name"><span class="brand-dot"></span><span>RIDGELINE<br>LENDING</span></div>
</section>

</body>
</html>
```